Christmas Postcard a manufacturer of skirting boards

Relaunch of the Christmas greetings Postcard of a company manufacturing premium quality skirting boards from real wood. Please refer to http://www.brumholt-profile.example/

- Christmas greetings Postcard 105 mm x 210 mm (card will be sent without envelope)

frontside:
- your graphic design, including
- Logo on the card
- Greetings "Frohe Weihnachten und ein erfolgreiches neues Jahr" on the card (front)
- insert Wooden Earring(s) - for recognition!

backside: (on the left)
"Wir bedanken uns für die partnerschaftliche Zusammenarbeit und freuen uns darauf, Sie auch im Jahr 2016 mit unseren Angeboten, Ideen und Know-how bei der Verwirklichung Ihrer Vorhaben zu unterstützen. (see pdf´s)

Ihnen und Ihren Mitarbeitern wünschen wir ein zauberhaftes Weihnachtsfest und für das neue Jahr Gesundheit, Glück, Erfolg und Freude."

Signatures (see pdf`s)

backside (on the right):
Adress field

------
The pdf´s from last years are just for the color mood. Fresh, modern design appreciated, no comic style.

Industry/Entity Type

It Company

Requirements
Must have
• "Wooden Earring(s)"

```html
<!DOCTYPE html>
<html lang="de">
<head>
<meta charset="utf-8">
<title>Brumholt Profile – Weihnachtskarte</title>
<link href="https://fonts.googleapis.com/css2?family=Jost:wght@400;600&family=Pinyon+Script&display=swap" rel="stylesheet">
<style>
  :root {
    --stage: #bdbec0;
    --card-tan: #e2b68a;
    --brand-red: #b8343f;
    --text-brown: #6e3b3b;
    --white: #ffffff;
    --photo-green: #1f7a3a;
    --photo-deep: #0e4d24;
    --photo-skin: #e9b9a0;
    --photo-light: #f4ddd0;
  }
  * { margin: 0; padding: 0; box-sizing: border-box; }
  html, body { width: 1198px; height: 1200px; overflow: hidden; background: var(--stage); }
  .canvas { position: relative; width: 1198px; height: 1200px; }
  .card {
    position: absolute; left: 137px; top: 137px; width: 924px; height: 925px;
    background: var(--card-tan); overflow: hidden;
  }
  .hero {
    position: absolute; left: 0; top: 0; width: 924px; height: 463px;
    background:
      radial-gradient(ellipse 380px 300px at 790px 330px, var(--photo-skin) 0%, #d99a7c 55%, rgba(160,90,60,0) 100%),
      radial-gradient(ellipse 300px 90px at 760px 30px, var(--photo-light) 0%, rgba(255,255,255,0) 100%),
      linear-gradient(100deg, var(--photo-deep) 0%, var(--photo-green) 40%, #4b7a3a 62%, #a8704d 80%, var(--photo-skin) 100%);
  }
  .hero__watermark {
    position: absolute; left: 40px; top: 325px;
    font-family: "Pinyon Script", cursive; font-size: 150px; line-height: 1;
    color: rgba(255,255,255,0.16); white-space: nowrap;
  }
  .hero__greeting {
    position: absolute; left: 30px; top: 272px; width: 470px;
    font-family: "Pinyon Script", cursive; color: var(--white);
    font-size: 46px; line-height: 0.75;
  }
  .hero__greeting span { display: block; }
  .hero__greeting .line-1 { padding-left: 35px; }
  .hero__greeting .line-2 { padding-left: 215px; font-size: 38px; }
  .brand-tag {
    position: absolute; left: 0; top: 100px; width: 298px; height: 93px;
    background: var(--card-tan); border-top: 6px solid var(--brand-red);
    display: flex; align-items: center; padding-left: 46px; gap: 14px;
  }
  .brand-tag__square { width: 22px; height: 22px; background: var(--brand-red); }
  .brand-tag__name {
    font-family: "Jost", sans-serif; font-weight: 600; font-size: 30px;
    color: var(--text-brown); letter-spacing: 1px;
  }
  .message {
    position: absolute; left: 0; top: 622px; width: 924px;
    font-family: "Jost", sans-serif; font-size: 17.5px; line-height: 23px;
    color: var(--text-brown); text-align: center;
  }
  .message__divider {
    width: 682px; margin: 10px auto 14px; border-top: 1px dotted rgba(255,255,255,0.7);
  }
</style>
</head>
<body>
<div class="canvas">
  <div class="card">
    <div class="hero" role="img" aria-label="Weihnachtsfoto: Kind mit Weihnachtsmütze und hölzernem S-Ohrring vor grünem, festlich geschmücktem Hintergrund"></div>
    <div class="hero__watermark" aria-hidden="true">Weihnachten</div>
    <div class="hero__greeting">
      <span class="line-1">Frohe Weihnachten</span>
      <span class="line-2">und</span>
      <span class="line-3">ein erfolgreiches neues Jahr</span>
    </div>
    <div class="brand-tag">
      <div class="brand-tag__square"></div>
      <div class="brand-tag__name">Brumholt Profile</div>
    </div>
    <div class="message">
      <p>Wir bedanken uns für die partnerschaftliche Zusammenarbeit und freuen<br>
      uns darauf, Sie auch im Jahr 2016 mit unseren Angeboten,<br>
      Ideen und Know-how bei der Verwirklichung Ihrer Vorhaben zu unterstützen.</p>
      <div class="message__divider"></div>
      <p>Ihnen und Ihren Mitarbeitern wünschen wir ein zauberhaftes Weihnachtsfest und<br>
      für das neue Jahr Gesundheit, Glück, Erfolg und Freude.</p>
    </div>
  </div>
</div>
</body>
</html>
```